Auto glazing business card design

need a business card design for my company, the logo will be provided with an inspirational design as well.
It is for an auto glazing business in Australia.
I would like to have the basic details on the card as my name, phone number, email adress and website.
I suppose the challenge will be to fit a long email adress on a small business card.

Target Market(s)

autoglazing customers, retail mostly

Industry/Entity Type

auto glazing

Contact Information for Business Card

logo, name, phone, email and website

Colors
0054AA
0677BA
7BADD7
CADEEF
E8F1F8
0094D4
00A9DD
6FCCEA
C7EBF8
E9F6FB

Requirements
Must have
• logo, business details, maybe QR code

```html
<!DOCTYPE html>
<html lang="en">
<head>
<meta charset="utf-8">
<title>ClearRoad Mobile Glazing – Business Card</title>
<link href="https://fonts.googleapis.com/css2?family=Lato:wght@400;700&display=swap" rel="stylesheet">
<style>
  :root {
    --backdrop: #8f8f8f;
    --navy: #061b34;
    --teal-light: #48b8ca;
    --teal-mid: #35a5c0;
    --teal-deep: #1f86ab;
    --white: #ffffff;
  }
  * { margin: 0; padding: 0; box-sizing: border-box; }
  html, body {
    width: 1200px; height: 1000px; overflow: hidden;
    background: var(--backdrop);
    font-family: "Lato", sans-serif;
  }
  .card {
    position: absolute;
    left: 290px;
    width: 629px; height: 359px;
    border-radius: 24px;
    overflow: hidden;
    box-shadow: 0 2px 6px rgba(0,0,0,0.25);
  }
  .card--front { top: 97px; }
  .card--back { top: 533px; background: var(--navy); }

  .front-artwork {
    position: absolute; inset: 0;
    background: radial-gradient(ellipse at 62% 42%, var(--teal-light) 0%, var(--teal-mid) 50%, var(--teal-deep) 100%);
  }

  .contact {
    position: absolute; left: 326px; top: 72px;
    color: var(--white);
  }
  .contact__name {
    font-weight: 700; font-size: 28px; letter-spacing: 0.2px; line-height: 1.2;
  }
  .contact__title {
    font-size: 16px; line-height: 1.2; margin-bottom: 11px;
  }
  .contact__list { list-style: none; font-size: 15px; letter-spacing: 0.2px; }
  .contact__item {
    display: flex; align-items: flex-start; line-height: 19.5px;
  }
  .contact__item--address { margin-bottom: 6px; }
  .contact__icon {
    width: 12px; height: 12px; margin: 4px 9px 0 1px; flex: none;
    fill: var(--white);
  }

  .brand {
    position: absolute; left: 0; right: 0; top: 170px;
    text-align: center; color: var(--white);
  }
  .brand__mark {
    display: block; width: 16px; height: 16px; margin: 0 auto 22px;
    background: var(--teal-mid);
  }
  .brand__name {
    font-weight: 700; font-size: 42px; letter-spacing: 12px; padding-left: 12px; line-height: 1;
  }
  .brand__tagline {
    font-weight: 400; font-size: 20px; letter-spacing: 12.5px; padding-left: 12.5px; margin-top: 12px; line-height: 1;
  }
</style>
</head>
<body>

<section class="card card--front">
  <div class="front-artwork" role="img" aria-label="Teal sweeping decorative artwork"></div>

  <div class="contact">
    <h1 class="contact__name">DANIEL HARTLEY</h1>
    <p class="contact__title">Founder &amp; CEO</p>
    <ul class="contact__list">
      <li class="contact__item contact__item--address">
        <svg class="contact__icon" viewBox="0 0 12 12"><path d="M6 0a4 4 0 0 0-4 4c0 3 4 8 4 8s4-5 4-8a4 4 0 0 0-4-4zm0 5.6A1.6 1.6 0 1 1 6 2.4a1.6 1.6 0 0 1 0 3.2z"/></svg>
        <span>Street Address Here, City<br>State, Country, ZIP 123</span>
      </li>
      <li class="contact__item">
        <svg class="contact__icon" viewBox="0 0 12 12"><path d="M2.5 0.5l2 2.3-1 1.3c.7 1.6 2 2.9 3.4 3.6l1.3-1 2.3 2-1.2 2.1C4.8 10.6 1.2 7 0.6 2z"/></svg>
        <span>(123) 456-7890</span>
      </li>
      <li class="contact__item">
        <svg class="contact__icon" viewBox="0 0 12 12"><path d="M3 0h6a1 1 0 0 1 1 1v10a1 1 0 0 1-1 1H3a1 1 0 0 1-1-1V1a1 1 0 0 1 1-1zm.5 1.5v7.5h5V1.5z"/></svg>
        <span>(123) 456-7890</span>
      </li>
      <li class="contact__item">
        <svg class="contact__icon" viewBox="0 0 12 12"><path d="M3 0h6v3H3zM1 4h10a1 1 0 0 1 1 1v4h-2v3H2V9H0V5a1 1 0 0 1 1-1zm2.5 4.5v2h5v-2z"/></svg>
        <span>(123) 456-7890</span>
      </li>
      <li class="contact__item">
        <svg class="contact__icon" viewBox="0 0 12 12"><path d="M0 2h12v8H0zm1 1v.4l5 3.3 5-3.3V3z"/></svg>
        <span>info@clearroadmobileglazing.com</span>
      </li>
      <li class="contact__item">
        <svg class="contact__icon" viewBox="0 0 12 12"><circle cx="6" cy="6" r="5.5"/><path fill="var(--teal-mid)" d="M3 3.5l2 .5 .5 2-1.5 1 .5 2.5-2-1.5zM7 2l2 1-1 1.5 1.5 2-1.5 2.5-1-2-.5-2z"/></svg>
        <span>clearroadmobileglazing.com</span>
      </li>
    </ul>
  </div>
</section>

<section class="card card--back">
  <div class="brand">
    <span class="brand__mark"></span>
    <p class="brand__name">CLEARROAD</p>
    <p class="brand__tagline">MOBILE GLAZING</p>
  </div>
</section>

</body>
</html>
```